Wine Bottle and Olive Oil Bottle Label

Design a bottle label for 'Calvera Estate'. The label should include a logo making use of the Republic of Formosa Lion image (stylized or slightly adjusted to avoid any copyright issues, although unlikely as any copyright would have expired) and/or the republic of formosa seal. Both of these images can be found by using google image search. For more information refer lorepedia here: https://en.lorepedia-example.org/wiki/Marovia_Seal

We need a label size suitable for use on both a while bottle approximately 70mm x 100mm and also 50mm x 100mm, and include enough space below the name+logo to print the type of wine e.g. "2017 Pinot Nior" or the words "Olive Oil".

Target Market(s)

Small Boutique Wine and Oil Oil market

Requirements
Must have
• Republic of Formosa Lion image (stylized or slightly adjusted to avoid any copyright issues, although unlikely as any copyright would have expired) and/or the republic of formosa seal. Include name 'Calvera Estate'. Space to add product type and year at bottom of label, with source files allowing this to be done. Work with two different label aspect ratios identifed in description

```html
<!DOCTYPE html>
<html lang="en">
<head>
<meta charset="utf-8">
<title>Calvera Estate – 2017 Pinot Noir Label</title>
<link href="https://fonts.googleapis.com/css2?family=Cinzel:wght@400;600;700&family=Uncial+Antiqua&display=swap" rel="stylesheet">
<style>
  :root {
    --gold: #ecc514;
    --gold-deep: #e5bb0c;
    --gold-soft: #f3d862;
    --gold-pale: #fdf6d8;
    --ink: #0d0d0d;
    --paper: #ffffff;
  }
  html, body {
    margin: 0;
    padding: 0;
    overflow: hidden;
    background: var(--paper);
  }
  .label {
    position: relative;
    width: 840px;
    height: 1200px;
    background: var(--paper);
    overflow: hidden;
  }
  .label__frame {
    position: absolute;
    inset: 0;
  }
  .ornament {
    position: absolute;
    border-radius: 40px;
    background: linear-gradient(90deg, transparent, var(--gold-soft) 22%, var(--gold) 50%, var(--gold-soft) 78%, transparent);
    opacity: 0.8;
  }
  .ornament--crown { left: 218px; top: 145px; width: 384px; height: 70px; }
  .ornament--upper { left: 258px; top: 852px; width: 322px; height: 38px; }
  .ornament--lower { left: 258px; top: 975px; width: 322px; height: 36px; }
  .estate-name {
    position: absolute;
    top: 268px;
    left: 0;
    width: 100%;
    margin: 0;
    text-align: center;
    font-family: "Uncial Antiqua", serif;
    font-weight: 400;
    font-size: 62px;
    letter-spacing: 3px;
    color: var(--gold);
    text-transform: uppercase;
  }
  .emblem {
    position: absolute;
    left: 175px;
    top: 370px;
    width: 470px;
    height: 470px;
  }
  .rule {
    position: absolute;
    left: 136px;
    width: 552px;
    height: 1px;
    background: var(--gold);
  }
  .rule--top { top: 893px; }
  .rule--bottom { top: 971px; }
  .product-name {
    position: absolute;
    top: 894px;
    left: 0;
    width: 100%;
    margin: 0;
    text-align: center;
    font-family: "Cinzel", serif;
    font-weight: 700;
    font-size: 60px;
    line-height: 78px;
    color: var(--ink);
  }
  .product-details {
    position: absolute;
    top: 1026px;
    left: 0;
    width: 100%;
    text-align: center;
    font-family: "Cinzel", serif;
    font-weight: 400;
    font-size: 27px;
    line-height: 34px;
    color: var(--gold-deep);
  }
  .product-details p { margin: 0; }
</style>
</head>
<body>
<main class="label">
  <svg class="label__frame" width="840" height="1200" viewBox="0 0 840 1200" aria-hidden="true">
    <path d="M62 212 H112 V162 H205 C225 95 290 60 420 60 C550 60 615 95 635 162 H728 V212 H778 V1000 H728 V1137 H112 V1000 H62 Z"
          fill="none" stroke="var(--gold)" stroke-width="24" stroke-linejoin="miter"/>
  </svg>

  <div class="ornament ornament--crown" role="img" aria-label="Gold flourish ornament"></div>

  <h1 class="estate-name">Calvera Estate</h1>

  <svg class="emblem" viewBox="0 0 470 470" role="img" aria-label="Estate emblem: stylised striped tiger over gold scrollwork inside a gold ring">
    <defs>
      <radialGradient id="emblem-fill" cx="50%" cy="50%" r="50%">
        <stop offset="0%" stop-color="var(--gold-soft)"/>
        <stop offset="100%" stop-color="var(--gold-pale)"/>
      </radialGradient>
    </defs>
    <circle cx="235" cy="235" r="222" fill="url(#emblem-fill)" stroke="var(--gold)" stroke-width="22"/>
  </svg>

  <div class="ornament ornament--upper" role="img" aria-label="Gold flourish ornament"></div>
  <div class="rule rule--top"></div>
  <h2 class="product-name">2017 Pinot Noir</h2>
  <div class="rule rule--bottom"></div>
  <div class="ornament ornament--lower" role="img" aria-label="Gold flourish ornament"></div>

  <div class="product-details">
    <p class="volume">1L</p>
    <p class="abv">10% v/v</p>
  </div>
</main>
</body>
</html>
```